Independent Consultant needs jazzy website for official company launch!

I need a simple (I think), 4-6 page wordpress design for a hosted wordpress site. I have a new logo for the company (it's a puzzle piece), and business cards but no other marketing materials developed yet.

The main features of the website are Services Offered and How Clients Use Us pages and a Resources section.

Section structure:
About us
Services Offered
How Clients Use Us
Blog
Resources

Blog items
I will use keywords and comments, categories and tags.
Images will be used and should be clickable to see larger picture.

Nature of business:
-Velbor Group, Inc. is a start-up independent management consulting firm based in the Twin Cities, MN but with affiliates in other US locations. We specialize in brain-based, research-based organization development, learning, and coaching services.
- my background: organization behavior, neuroscience, training design and delivery, change management, management coaching, facilitation

Favourite colors:
- citron green
-orange
-grey
-blues - not turqoise or teal

Updates
•Instead of creating a bunch of custom css/html, i would like the final design to be based on one of these themes (these are my favorites):
Quillwhistle, Bramblet, UPelk, Lovisture, Odask, Fenwisha, Marlowbe, Glimbers, Vusko, Halberquint)

Target Market(s)
business owners, executives, mid-upper level managers in private and public sector companies

Examples of sites I kind of like:
http://www.trosnik-example.com
Updates

                                        I am posting a scanned front and back business card to give you an idea of the style I've used so far.  Thank you!

Industry/Entity Type

Management Consulting

Requirements
Must have
• resources page must be set up like a small store - i'll want to sell books, training materials from this site

also would like to build a mailing list over time so that i can send a periodic newsletter to visitors
Should not have
• difficult updates or require me to hire someone to make simple content edits - i'd like to do that on my own

don't want a lot of 'generic' people in photos on my site - would rather have a few real photos included or some visuals of symbols or objects that relate to the work provided

like bold, modern look but not too cutesy or young looking

```html
<!DOCTYPE html>
<html lang="en">
<head>
<meta charset="utf-8">
<title>Velbor Group, Inc. — Blog</title>
<link rel="stylesheet" href="https://fonts.googleapis.com/css2?family=Ubuntu:wght@400;500;700&family=Arimo:wght@400;700&family=Montserrat:wght@500;600&display=swap">
<style>
:root{
  --page:#333333;
  --nav:#5b9540;
  --nav-active:#4d8537;
  --frame:#8fb43a;
  --panel:#eff0f2;
  --card:#ffffff;
  --orange:#e0600f;
  --ink:#333333;
  --body:#4a4a4a;
  --muted:#8a8a8a;
  --rule:#c9cacc;
  --bar:#6b6b6b;
}
*{box-sizing:border-box;margin:0;padding:0}
html,body{width:1062px;height:1200px;overflow:hidden;background:var(--page);font-family:"Arimo",Arial,sans-serif;color:var(--body)}
.canvas{position:relative;width:1062px;height:1200px}

/* header */
.brand-mark{position:absolute;left:133px;top:16px;width:118px;height:118px;background:#8bb43f}
.brand-name{position:absolute;left:257px;top:14px;font-family:"Ubuntu",sans-serif;font-weight:700;font-size:38px;color:#fff;letter-spacing:.5px}
.tagline{position:absolute;left:257px;top:64px;font-family:"Ubuntu",sans-serif;font-size:23px;color:#fff}
.social-top{position:absolute;left:916px;top:57px;display:flex;gap:8px}
.social-top span{width:29px;height:29px;border-radius:50%;background:#fff}
.nav-box{position:absolute;left:257px;top:102px;width:33px;height:32px;border:2px solid var(--nav)}
.main-nav{position:absolute;left:293px;top:102px;display:flex;height:32px;background:var(--nav)}
.main-nav a{display:flex;align-items:center;justify-content:center;color:#fff;text-decoration:none;font-family:"Ubuntu",sans-serif;font-size:12.5px;border-right:1px solid #6ea854}
.main-nav a:last-child{border-right:0}
.main-nav a.active{background:var(--nav-active)}

/* slider */
.slider{position:absolute;left:80px;top:152px;width:903px;height:287px;background:var(--frame)}
.slide-photo{position:absolute;left:7px;top:7px;width:889px;height:272px;border:2px solid #e6e8ea;background:linear-gradient(90deg,#e3e6e9 0%,#c9c3bb 30%,#8aa1bd 62%,#eef0f3 80%,#f4f5f7 100%)}
.slide-title{position:absolute;left:629px;top:80px;font-family:"Ubuntu",sans-serif;font-size:28px;color:var(--ink)}
.slide-arrow{position:absolute;top:133px}

/* content */
.content{position:absolute;left:80px;top:448px;width:903px;height:698px;background:var(--panel)}
.section-title{position:absolute;left:14px;top:22px;font-family:"Ubuntu",sans-serif;font-size:22px;color:var(--orange)}
.post{position:absolute;left:14px;width:614px;height:190px;border-bottom:1px solid var(--rule)}
.post-thumb{position:absolute;left:0;top:0;width:176px;height:110px;border:3px solid #d4d5d7}
.post-title{position:absolute;left:193px;top:1px;font-family:"Montserrat",sans-serif;font-weight:500;font-size:16.5px;color:var(--ink)}
.post-excerpt{position:absolute;left:194px;top:36px;width:420px;font-size:11.6px;line-height:18.5px;text-align:justify;color:var(--body)}
.post-meta{position:absolute;left:0;top:130px;width:614px;display:flex;align-items:center;font-size:11.6px;color:var(--body)}
.post-meta a{color:var(--orange);text-decoration:none}
.bubble{width:18px;height:12px;margin-right:10px}
.meta-more{width:103px}
.meta-tags{width:229px}
.meta-author{width:167px}
.share{display:flex;gap:5px}
.share span{height:11px;border:1px solid #c6cfdc;background:#fff}

.pagination{position:absolute;left:316px;top:666px;display:flex;align-items:center;gap:3px;font-size:10px;color:#555}
.pagination .label{margin-right:3px}
.pagination .pg{width:21px;height:20px;border-radius:3px;background:#d2d3d5;color:#fff;display:flex;align-items:center;justify-content:center}
.pagination .pg.current{background:#8a8b8d}
.pagination .gap{width:20px;text-align:center;color:#999}

/* sidebar */
.subscribe{position:absolute;left:662px;top:17px;width:246px;height:305px;background:var(--card);padding:10px 18px}
.widget-title{font-family:"Montserrat",sans-serif;font-weight:500;font-size:16px;color:var(--ink);letter-spacing:.5px;padding-bottom:8px;border-bottom:1px solid var(--rule)}
.subscribe p{margin-top:12px;font-size:11.2px;line-height:16.6px;color:var(--muted);text-align:justify;padding:0 2px}
.feeds{display:flex;gap:22px;margin-top:18px;padding-left:12px}
.feed{display:flex;flex-direction:column;align-items:center;width:40px;font-size:9.5px;color:#444}
.feed span{width:28px;height:28px;border-radius:4px;margin-bottom:5px}
.feed .rss{background:#f08a24}.feed .f1{background:#4a6aa5}.feed .f2{background:#6fc9e6}
.email-title{display:flex;align-items:center;gap:8px;margin-top:20px;font-family:"Montserrat",sans-serif;font-weight:500;font-size:14px;color:var(--ink)}
.email-form{display:flex;margin-top:9px}
.email-form span{width:130px;height:22px;border:1px solid #b8b8b8;border-radius:3px 0 0 3px;background:#fff}
.email-form b{width:65px;height:22px;background:#2e2e2e;color:#fff;font-weight:400;font-size:11.5px;display:flex;align-items:center;justify-content:center;border-radius:0 3px 3px 0}

.popular{position:absolute;left:663px;top:337px;width:244px}
.popular h3{height:23px;background:var(--bar);color:#fff;font-family:"Montserrat",sans-serif;font-weight:500;font-size:14.5px;padding:3px 14px;letter-spacing:.3px}
.popular ul{list-style:none;margin-top:12px;padding:0 11px 0 12px}
.popular li{font-size:11.5px;line-height:18.5px;color:var(--body);padding:5px 2px 8px;border-bottom:2px solid #d6d7d9}
.popular li+li{padding-top:10px}

.footer{position:absolute;left:0;top:1168px;width:1062px;text-align:center;font-family:"Ubuntu",sans-serif;font-size:12px;color:#ddd}
</style>
</head>
<body>
<div class="canvas">

  <header>
    <div class="brand-mark"></div>
    <div class="brand-name">Velbor Group, Inc.</div>
    <div class="tagline">Helping people and organizations thrive!</div>
    <div class="social-top"><span></span><span></span></div>
    <div class="nav-box"></div>
    <nav class="main-nav">
      <a class="active" style="width:84px">HOME</a>
      <a style="width:104px">ABOUT US</a>
      <a style="width:147px">SERVICES OFFERED</a>
      <a style="width:164px">HOW CLIENTS USE US</a>
      <a style="width:76px">BLOG</a>
      <a style="width:115px">RESOURCES</a>
    </nav>
  </header>

  <section class="slider">
    <div class="slide-photo" role="img" aria-label="Photo of a business team seated around a meeting table in a bright office">
      <div class="slide-title">Contantry Popular</div>
      <svg class="slide-arrow" style="left:19px" width="22" height="36" viewBox="0 0 22 36"><path d="M19 2 4 18l15 16" fill="none" stroke="#8a8a8a" stroke-width="3.5"/></svg>
      <svg class="slide-arrow" style="left:850px" width="22" height="36" viewBox="0 0 22 36"><path d="M3 2l15 16L3 34" fill="none" stroke="#8a8a8a" stroke-width="3.5"/></svg>
    </div>
  </section>

  <main class="content">
    <h1 class="section-title">Blog</h1>

    <article class="post" style="top:75px">
      <div class="post-thumb" role="img" aria-label="Photo of a smiling businessman in a suit in an office" style="background:linear-gradient(135deg,#e9edf1,#5d7799 55%,#d8dde3)"></div>
      <h2 class="post-title">Sedut perspiciatis unde voluptatem accusantium</h2>
      <p class="post-excerpt">Nemo enim ipsam voluptatem quia voluptas sit aspernatur aut odit aut fugit, sed quia consequuntur magni dolores eos qui ratione voluptatem sequi nesciunt. Neque porro quisquam est, qui dolorem ipsum quia dolor sit amet, consectetur, adipisci velit, sed quia non numquam eius modi.</p>
      <div class="post-meta">
        <svg class="bubble" viewBox="0 0 18 12"><ellipse cx="9" cy="5" rx="8.5" ry="4.5" fill="#e8821e"/><path d="M5 8 4 12l5-3z" fill="#e8821e"/></svg>
        <span class="meta-more"><a>Read More</a></span>
        <span class="meta-tags">Tags: <a>marketing analytics</a>, <a>intermediate</a></span>
        <span class="meta-author">Posted by <a>Della Prewitt</a></span>
        <span class="share"><span style="width:32px"></span><span style="width:15px"></span><span style="width:40px"></span><span style="width:19px"></span></span>
      </div>
    </article>

    <article class="post" style="top:274px">
      <div class="post-thumb" role="img" aria-label="Photo of a businesswoman with colleagues in a meeting" style="background:linear-gradient(135deg,#dfe2e6,#3a3d44 55%,#e4e6ea)"></div>
      <h2 class="post-title">Sedut perspiciatis unde voluptatem accusantium</h2>
      <p class="post-excerpt">Nemo enim ipsam voluptatem quia voluptas sit aspernatur aut odit aut fugit, sed quia consequuntur magni dolores eos qui ratione voluptatem sequi nesciunt. Neque porro quisquam est, qui dolorem ipsum quia dolor sit amet, consectetur, adipisci velit, sed quia non numquam eius modi.</p>
      <div class="post-meta">
        <svg class="bubble" viewBox="0 0 18 12"><ellipse cx="9" cy="5" rx="8.5" ry="4.5" fill="#e8821e"/><path d="M5 8 4 12l5-3z" fill="#e8821e"/></svg>
        <span class="meta-more"><a>Read More</a></span>
        <span class="meta-tags">Tags: <a>marketing analytics</a>, <a>intermediate</a></span>
        <span class="meta-author">Posted by <a>Della Prewitt</a></span>
        <span class="share"><span style="width:32px"></span><span style="width:15px"></span><span style="width:40px"></span><span style="width:19px"></span></span>
      </div>
    </article>

    <article class="post" style="top:474px">
      <div class="post-thumb" role="img" aria-label="Photo of a presenter at a flip chart in a boardroom" style="background:linear-gradient(90deg,#c9962e,#6b5a3a 40%,#ece9e4 70%,#8c7f70)"></div>
      <h2 class="post-title">Sedut perspiciatis unde voluptatem accusantium</h2>
      <p class="post-excerpt">Nemo enim ipsam voluptatem quia voluptas sit aspernatur aut odit aut fugit, sed quia consequuntur magni dolores eos qui ratione voluptatem sequi nesciunt. Neque porro quisquam est, qui dolorem ipsum quia dolor sit amet, consectetur, adipisci velit, sed quia non numquam eius modi.</p>
      <div class="post-meta">
        <svg class="bubble" viewBox="0 0 18 12"><ellipse cx="9" cy="5" rx="8.5" ry="4.5" fill="#e8821e"/><path d="M5 8 4 12l5-3z" fill="#e8821e"/></svg>
        <span class="meta-more"><a>Read More</a></span>
        <span class="meta-tags">Tags: <a>marketing analytics</a>, <a>intermediate</a></span>
        <span class="meta-author">Posted by <a>Della Prewitt</a></span>
        <span class="share"><span style="width:32px"></span><span style="width:15px"></span><span style="width:40px"></span><span style="width:19px"></span></span>
      </div>
    </article>

    <div class="pagination">
      <span class="label">Page 1 of 32</span>
      <span class="pg current">1</span><span class="pg">2</span><span class="pg">3</span><span class="pg">4</span><span class="pg">5</span><span class="pg">6</span><span class="pg">7</span><span class="pg">8</span><span class="pg">»</span><span class="gap">…</span><span class="pg">»»</span>
    </div>

    <aside class="subscribe">
      <h3 class="widget-title">SUBSCRIBE</h3>
      <p>Nemo enim ipsam voluptatem quia voluptas sit aspernatur aut odit aut fugit, sed quia consequuntur magni dolores eos qui ratione voluptatem sequi nesciunt. Neque porro quisquam est, qui dolorem ipsum quia.</p>
      <div class="feeds">
        <div class="feed"><span class="rss"></span>RSS</div>
        <div class="feed"><span class="f1"></span>Friendloop</div>
        <div class="feed"><span class="f2"></span>Chirpline</div>
      </div>
      <div class="email-title">
        <svg width="15" height="11" viewBox="0 0 15 11"><rect x=".5" y=".5" width="14" height="10" fill="none" stroke="#777"/><path d="M.5.5 7.5 6l7-5.5" fill="none" stroke="#777"/></svg>
        Subscribe by email
      </div>
      <div class="email-form"><span></span><b>Subscribe</b></div>
    </aside>

    <aside class="popular">
      <h3>Most Popular Post</h3>
      <ul>
        <li>Nulla fermentum purus ut justo cursus viverra luctus pulvinar</li>
        <li>Aenean dapibus lacus a urna</li>
        <li>Ut eu ipsum vestibulum purus sollicitu adipiscing ac sit amet sapien</li>
        <li>Mauris quis augue eget quam gravida dapibus vel quis</li>
        <li>Fusce imperdiet ipsum eget dolor tincid unt eget suscipit mi feugiat fermentum purus ut justo cursus tempus</li>
      </ul>
    </aside>
  </main>

  <footer class="footer">Copyright © 2012 www.velborgroupinc.com &nbsp;&nbsp; All rights reserved.</footer>
</div>
</body>
</html>
```